Webdesign für Einrichtungsunternehmen
Zielgruppe
Die Brando Raumkonzept GmbH gestaltet als Inneneinrichter, Raumdesigner und Büroausstatter Geschäftsräume aller Art (Geschäfts-, Praxis- und Büroräume). Als Fachmann für Ladenbau berät das Team dessen Kunden auch bei der Konzeption und ist bei der Auswahl der Materialien behilflich. Des weiteren können auch private Kunden individuelle Möbel und Einrichtungslösungen erhalten.
Die Zielgruppen sind: Planer, Architekten, Privatkunden
Aufgabenstellung
- als PSD
- das Layout soll sich von der jetzigen Website stark unterscheiden
- neben dem 'Ladenbau' soll der Bereich 'Exclusive Wohnraumlösungen' die gleiche Wertigkeit erhalten.
- der Punkt 'Service' beinhaltet 'Beratung und Planung', die 'Fertigung' und 'Lohnarbeit'
- der Nutzer soll mit einem Slogan begrüst werden - hier bitten wir um Ihre kreativen Ideen
- eine mitlaufende Kontaktleiste einarbeiten (Slide out right- Popup)

```html
<!DOCTYPE html>
<html lang="de">
<head>
<meta charset="utf-8">
<title>Brando Raumkonzept GmbH – Ladenbau Zwickau</title>
<link href="https://fonts.googleapis.com/css2?family=Plus+Jakarta+Sans:wght@400;500;600;700&display=swap" rel="stylesheet">
<style>
:root{
  --red:#f0402b;
  --ink:#141414;
  --text:#2b2b2b;
  --grey-bg:#f4f4f4;
  --page-bg:#f5f6f8;
  --white:#ffffff;
  --line:#333;
}
*{box-sizing:border-box;margin:0;padding:0}
html,body{width:1200px;height:3625px;overflow:hidden;background:var(--page-bg);font-family:"Plus Jakarta Sans",sans-serif;color:var(--text)}
.site{position:absolute;left:46px;top:49px;width:1107px;height:3524px;background:var(--white);box-shadow:0 10px 40px rgba(0,0,0,.06);border-radius:6px;overflow:hidden}
.abs{position:absolute}
.header{left:0;top:0;width:1107px;height:61px;background:var(--white)}
.brand{display:flex;align-items:center;gap:8px}
.brand-mark{width:22px;height:22px;background:var(--red)}
.brand-name{font-weight:700;font-size:15px;color:var(--red)}
.header .brand{position:absolute;left:86px;top:19px}
.nav{position:absolute;right:87px;top:23px;display:flex;gap:19px;font-size:11px;color:var(--ink)}
.hero{left:0;top:61px;width:1107px;height:517px;background:linear-gradient(110deg,#1d2a3a 0%,#2c4560 35%,#6b5a4a 65%,#3a3431 100%)}
.hero h1{position:absolute;left:86px;top:320px;font-size:38px;line-height:46px;font-weight:600;color:var(--white);letter-spacing:-.5px;width:400px}
.btn{display:inline-flex;align-items:center;justify-content:center;gap:8px;background:var(--red);color:var(--white);font-size:11px;font-weight:600;height:33px;padding:0 14px}
.hero .btn{position:absolute;left:86px;top:450px}
.side-tab{left:1074px;top:257px;width:33px;height:139px;background:var(--red);display:flex;flex-direction:column;align-items:center;justify-content:center;gap:8px}
.side-tab span{writing-mode:vertical-rl;transform:rotate(180deg);color:var(--white);font-size:10px;font-weight:500}
.band-grey{background:var(--grey-bg)}
.eyebrow{font-size:12px;color:var(--red);margin-bottom:8px}
.title{font-size:29px;line-height:33px;font-weight:600;color:var(--ink);letter-spacing:-.3px}
.rule{width:50px;height:4px;background:var(--red);margin-top:14px}
.copy{font-size:11.5px;line-height:18.5px;color:var(--text)}
.copy p+p{margin-top:12px}
.photo{display:block}
.contact-form label{display:block;font-size:11px;color:var(--ink);margin-bottom:5px}
.field{border:1px solid var(--line);background:var(--white)}
.check{display:flex;align-items:center;gap:10px;font-size:11px}
.check i{width:15px;height:15px;border:1px solid var(--line);display:block}
.footer{font-size:11px;color:var(--ink)}
.footer h4{font-size:11px;font-weight:600}
.socials{display:flex;gap:18px}
.socials i{width:12px;height:12px;border-radius:50%;background:var(--red);display:block}
</style>
</head>
<body>
<div class="site">
  <header class="header abs">
    <div class="brand"><span class="brand-mark"></span><span class="brand-name">Brando Raumkonzept GmbH</span></div>
    <nav class="nav"><span>Ladenbau</span><span>Exclusive Wohnraumlösungen</span><span>Service</span><span>Inspirationen</span><span>Unternehmen</span><span>News</span><span>Jobs</span><span>Kontakt</span></nav>
  </header>

  <section class="hero abs" role="img" aria-label="Foto: Verkäuferin an einer Café-Theke mit Gebäck bedient einen Kunden">
    <h1>Machen Sie Ihr Geschäft zu mehr als nur einem Geschäft</h1>
    <a class="btn">Kontaktieren Uns</a>
  </section>

  <div class="side-tab abs">
    <span>Kontaktieren Uns</span>
    <svg width="12" height="12" viewBox="0 0 24 24" fill="none" stroke="#fff" stroke-width="2"><path d="M5 3h4l2 5-3 2a12 12 0 0 0 6 6l2-3 5 2v4a2 2 0 0 1-2 2A18 18 0 0 1 3 5a2 2 0 0 1 2-2z"/></svg>
  </div>

  <section class="band-grey abs" style="left:0;top:578px;width:1107px;height:309px">
    <div class="abs" style="left:86px;top:85px">
      <div class="eyebrow">Brando Raumkonzept GmbH</div>
      <h2 class="title">Ihr Fachmann für<br>Ladenbau in Zwickau</h2>
      <div class="rule"></div>
    </div>
    <div class="copy abs" style="left:646px;top:83px;width:376px">
      <p>Sie wünschen sich eine maßgefertigte Inneneinrichtung passend zu Ihrem Ladenkonzept und möchten Ihr Geschäft teilweise oder sogar komplett neu einrichten? Dann freuen wir uns auf Ihren Kontakt. Wir gestalten als Inneneinrichter, Raumdesigner und Büroausstatter Geschäftsräume aller Art.</p>
      <p>Als Fachmann für Ladenbau beraten wir Sie auch bei der Konzeption und sind Ihnen bei der Auswahl der Materialien behilflich. Die Kosten werden kundenfreundlich kalkuliert.</p>
    </div>
  </section>

  <section class="abs" style="left:0;top:887px;width:1107px;height:479px">
    <div class="photo abs" role="img" aria-label="Foto: Mitarbeiter an einer Kantenanleimmaschine in der Werkstatt" style="left:0;top:0;width:566px;height:479px;background:linear-gradient(120deg,#e9ecef 0%,#cfd5db 45%,#8d99a6 80%,#3b4654 100%)"></div>
    <div class="abs" style="left:646px;top:69px;width:376px">
      <div class="eyebrow">Brando Raumkonzept GmbH</div>
      <h2 class="title">Wir erfüllen Ihre<br>Einrichtungswünsche</h2>
      <div class="copy" style="margin-top:28px">
        <p>Dank unserer langjährigen Erfahrung können wir Ihre Vorstellungen in die Realität umsetzen. Die Brando Raumkonzept GmbH führt die Objekteinrichtungen in Ihren Geschäfts-, Praxis- und Büroräumen fachmännisch und passgenau durch, dass Ihre Einrichtungswünsche Wirklichkeit werden.</p>
        <p>Selbstverständlich können Sie bei uns auch Möbel und Einrichtungslösungen für Ihren privaten Haushalt in Auftrag geben</p>
      </div>
      <a class="btn" style="margin-top:22px">Kontaktieren Uns</a>
    </div>
  </section>

  <section class="band-grey abs" style="left:0;top:1366px;width:1107px;height:309px">
    <div class="abs" style="left:86px;top:77px">
      <div class="eyebrow">Individuelle Ladenbau-Konzepte</div>
      <h2 class="title">Exklusive<br>Objekteinrichtungen</h2>
      <div class="rule"></div>
    </div>
    <div class="copy abs" style="left:646px;top:76px;width:376px">
      <p>Wir führen unsere Aufträge im Ladenbau und Objekteinrichtungen penibel, sensibel und bis ins kleinste Detail professionell aus. Mit unserer Inneneinrichtung wollen wir einen großen Beitrag zu Ihrem Unternehmenserfolg beitragen. Deshalb schätzen unsere Kunden höchste Qualität und Präzision. Setzen auch Sie auf namenhafte Hersteller und lassen Sie sich mit dem richtigen Stil begeistern. Auf Wunsch werden wir Ihre Möbelstücke dem neuen Einrichtungskonzept anpassen und aufwerten oder restaurieren.</p>
    </div>
  </section>

  <section class="abs" style="left:0;top:1675px;width:1107px;height:481px">
    <div class="abs" style="left:86px;top:106px;width:376px">
      <div class="eyebrow">Brando Raumkonzept GmbH</div>
      <h2 class="title">Ihr Profi für<br>Sonderanfertigungen</h2>
      <div class="copy" style="margin-top:28px">
        <p>Unser erfahrenes Team verfügt über eine bestens ausgestattete Werkstatt, um Ihre Sonderwünsche professionell und passgenau umsetzen zu können. So können wir auf Wunsch Ihre Möbel nach Entwürfen bauen oder flexibel und individuell Sonderanfertigungen ausführen oder Ihr bestehendes Mobiliar anpassen.</p>
      </div>
      <a class="btn" style="margin-top:22px">Kontaktieren Uns</a>
    </div>
    <div class="photo abs" role="img" aria-label="Visualisierung: leerer Verkaufsraum mit Wandregalen und Holzsockeln" style="left:542px;top:0;width:565px;height:481px;background:linear-gradient(180deg,#d9dadd 0%,#c9c3a8 35%,#b9b196 70%,#9aa4a6 100%)"></div>
  </section>

  <section class="band-grey abs" style="left:0;top:2156px;width:1107px;height:422px">
    <div class="abs" style="left:86px;top:64px">
      <div class="eyebrow">Inspirationen</div>
      <h2 class="title">Aktuelles Projekt</h2>
    </div>
    <div class="photo abs" role="img" aria-label="Projektfoto: Apotheke mit weißer Theke und Holzboden" style="left:86px;top:136px;width:215px;height:234px;background:linear-gradient(160deg,#f3ede6,#d99a6b 60%,#b9a18a)"></div>
    <div class="photo abs" role="img" aria-label="Projektfoto: Verkaufsraum mit Holzdecke und grünen Regalen" style="left:326px;top:136px;width:215px;height:234px;background:linear-gradient(160deg,#e8e2d6,#b58a5e 45%,#9fcf7a 75%,#c9a783)"></div>
    <div class="photo abs" role="img" aria-label="Projektfoto: Apotheke mit grünen Regalsystemen" style="left:566px;top:136px;width:215px;height:234px;background:linear-gradient(160deg,#ece9ef,#8e6aa0 45%,#6fc36a 75%,#bfa98f)"></div>
    <div class="photo abs" role="img" aria-label="Projektfoto: Apotheke mit dunklen Holzregalen" style="left:806px;top:136px;width:215px;height:234px;background:linear-gradient(160deg,#f2e4cf,#8a5a3a 45%,#6b4a35 70%,#c7a57d)"></div>
    <div class="photo abs" role="img" aria-label="Projektfoto: heller Verkaufsraum mit Regalen" style="left:1046px;top:136px;width:61px;height:234px;background:linear-gradient(160deg,#eee6d8,#c9b59a)"></div>
  </section>

  <section class="abs contact-form" style="left:0;top:2578px;width:1107px;height:620px">
    <div class="abs" style="left:86px;top:104px">
      <div class="eyebrow">Kontakt</div>
      <h2 class="title">Kontakt &amp; Anfahrt</h2>
    </div>
    <div class="abs" style="left:86px;top:183px"><label>Vorname</label><div class="field" style="width:176px;height:36px"></div></div>
    <div class="abs" style="left:286px;top:183px"><label>Nachname</label><div class="field" style="width:176px;height:36px"></div></div>
    <div class="abs" style="left:86px;top:257px"><label>E-mail</label><div class="field" style="width:376px;height:36px"></div></div>
    <div class="abs" style="left:86px;top:333px"><label>Nachricht</label><div class="field" style="width:376px;height:98px"></div></div>
    <div class="check abs" style="left:86px;top:471px"><i></i><span>Sie stimmen unserer freundlichen Datenschutzerklärung zu.</span></div>
    <a class="btn abs" style="left:86px;top:508px;width:116px">Senden
      <svg width="12" height="12" viewBox="0 0 24 24" fill="none" stroke="#fff" stroke-width="2"><path d="M22 2 11 13M22 2l-7 20-4-9-9-4z"/></svg>
    </a>
    <div class="photo abs" role="img" aria-label="Stadtplan von Zwickau mit Firmenstandort" style="left:590px;top:94px;width:430px;height:460px;background:linear-gradient(135deg,#e6e1d8,#d9dcc8 40%,#e8d5d2 70%,#dcd8cc);border:1px solid #ccc">
      <div class="abs" style="left:8px;top:8px;width:22px;height:44px;background:#fff;border:1px solid #bbb;font-size:14px;text-align:center;line-height:21px;color:#333">+<br>−</div>
    </div>
  </section>

  <footer class="footer abs" style="left:0;top:3198px;width:1107px;height:326px">
    <div class="brand abs" style="left:86px;top:72px"><span class="brand-mark"></span><span class="brand-name">Brando Raumkonzept GmbH</span></div>
    <div class="abs" style="left:86px;top:122px;line-height:21px">
      <div>Telefon 0375 41209375</div>
      <div>info@brando-raumkonzept.de</div>
      <div>Lindenhofweg 14 | 08056 Zwickau</div>
      <h4 style="margin-top:13px">Folgen Sie uns</h4>
      <div class="socials" style="margin-top:9px"><i></i><i></i><i></i></div>
    </div>
    <div class="abs" style="left:770px;top:64px;line-height:14px">
      <h4>Navigation</h4>
      <div style="margin-top:23px">Ladenbau</div>
      <div style="margin-top:13px">Exclusive<br>Wohnraumlösungen</div>
      <div style="margin-top:13px">Service</div>
      <div style="margin-top:13px">Insoirationen</div>
      <div style="margin-top:13px">News</div>
      <div style="margin-top:13px">Job</div>
      <div style="margin-top:13px">Kontakt</div>
    </div>
    <div class="abs" style="left:956px;top:64px;line-height:26px">
      <div>Impressum</div>
      <div>Datenschutz</div>
      <div>Sitemap</div>
    </div>
  </footer>
</div>
</body>
</html>
```